10th Anniversary Grand Prize Giveaway

I need an A3 poster that we can display in our clinics to show that it is our 10th anniversary and that we are going to be having loads of promotions and a Grand Prize Giveaway. For all clients, we are offering 10% discount on all our packages. For the prize giveaway, everyone who visits our clinics during October gets entered into a prize draw. The main prize is One year chiropractic wellness care. There are a variety of other prizes. I need you to take the images of the prizes and make one image please. Our corporate colour is blue. I am attaching all info.

Target Market(s)

Our chiropractic patients

Industry/Entity Type

Health And Wellness

Font styles to use
Serif

Colors
0455a3

Requirements
Must have
• Included on brief
Nice to have
• Included on brief
Should not have
• Included on brief

```html
<!DOCTYPE html>
<html lang="en">
<head>
<meta charset="utf-8">
<title>10th Anniversary Grand Prize Giveaway</title>
<link rel="stylesheet" href="https://fonts.googleapis.com/css2?family=Baloo+2:wght@800&family=Open+Sans:ital,wght@0,400;0,700;0,800;1,400;1,700&family=Playfair+Display:wght@900&display=swap">
<style>
  :root {
    --blue-deep: #0b2a78;
    --blue-brand: #0455a3;
    --blue-light: #3fa3ec;
    --blue-ice: #9fd6ff;
    --navy: #16226a;
    --yellow: #fff200;
    --gold: #c8902a;
    --gold-light: #e6b24a;
    --red: #d7262e;
    --red-dark: #9e1a20;
    --white: #ffffff;
    --ink: #1e2a4a;
  }
  html, body { margin: 0; padding: 0; overflow: hidden; background: #ffffff; }
  .poster { display: block; width: 849px; height: 1200px; }
  .sans { font-family: "Open Sans", Arial, sans-serif; }
  .display-serif { font-family: "Playfair Display", Georgia, serif; font-weight: 900; }
  .rounded { font-family: "Baloo 2", "Arial Rounded MT Bold", sans-serif; font-weight: 800; }
</style>
</head>
<body>
<svg class="poster" viewBox="0 0 849 1200" xmlns="http://www.w3.org/2000/svg">
  <defs>
    <radialGradient id="bg-glow" cx="0.5" cy="0.33" r="0.75">
      <stop offset="0" stop-color="#2f8fe6"/>
      <stop offset="0.45" stop-color="#0455a3"/>
      <stop offset="1" stop-color="#0b2a78"/>
    </radialGradient>
    <linearGradient id="gold-fill" x1="0" y1="0" x2="1" y2="1">
      <stop offset="0" stop-color="#e9b955"/>
      <stop offset="1" stop-color="#b57b1e"/>
    </linearGradient>
    <radialGradient id="soft-spot">
      <stop offset="0" stop-color="#bfe6ff" stop-opacity="0.55"/>
      <stop offset="1" stop-color="#bfe6ff" stop-opacity="0"/>
    </radialGradient>
  </defs>

  <!-- background -->
  <rect class="backdrop" width="849" height="1200" fill="url(#bg-glow)"/>
  <g class="light-spots">
    <circle cx="620" cy="250" r="120" fill="url(#soft-spot)"/>
    <circle cx="230" cy="320" r="90" fill="url(#soft-spot)"/>
    <circle cx="720" cy="420" r="70" fill="url(#soft-spot)"/>
  </g>
  <g class="swooshes" fill="none">
    <path d="M0 60 C200 120 360 40 560 0" stroke="var(--blue-ice)" stroke-opacity="0.35" stroke-width="30"/>
    <path d="M0 300 C160 200 380 120 849 150" stroke="var(--blue-light)" stroke-opacity="0.25" stroke-width="40"/>
    <path d="M420 1200 C620 1100 760 980 849 760" stroke="var(--blue-ice)" stroke-opacity="0.45" stroke-width="26"/>
    <path d="M600 1200 C720 1120 810 1040 849 960" stroke="var(--blue-light)" stroke-opacity="0.55" stroke-width="30"/>
  </g>

  <!-- clinic name -->
  <g class="clinic-name">
    <rect x="290" y="0" width="222" height="78" fill="var(--white)"/>
    <circle cx="308" cy="40" r="8" fill="var(--blue-brand)"/>
    <text x="322" y="46" class="sans" font-weight="700" font-size="15" fill="var(--blue-brand)" textLength="176" lengthAdjust="spacingAndGlyphs">CoreWell Chiropractic</text>
  </g>

  <!-- discount badge -->
  <g class="discount-badge">
    <circle cx="123" cy="150" r="84" fill="var(--white)"/>
    <circle cx="123" cy="150" r="79" fill="url(#gold-fill)"/>
    <circle cx="123" cy="150" r="73" fill="none" stroke="var(--white)" stroke-width="1.5"/>
    <g class="sans" font-weight="700" fill="var(--white)" text-anchor="middle" font-size="10.5">
      <text x="123" y="96">BUY A</text>
      <text x="123" y="109">NEW PACKAGE,</text>
      <text x="123" y="122">OR UPGRADE YOUR</text>
      <text x="123" y="135">CURRENT ONE, DURING</text>
      <text x="123" y="148">OCTOBER TO ENJOY A</text>
    </g>
    <text x="123" y="176" text-anchor="middle" class="display-serif" font-size="28" fill="var(--white)">10%</text>
    <text x="123" y="201" text-anchor="middle" class="display-serif" font-size="22" fill="var(--white)" textLength="98" lengthAdjust="spacingAndGlyphs">DISCOUNT</text>
    <text x="123" y="216" text-anchor="middle" class="sans" font-size="8" fill="var(--white)">★ ★ ★</text>
  </g>

  <!-- anniversary mark -->
  <g class="anniversary-mark">
    <text x="292" y="465" class="sans" font-weight="800" font-style="italic" font-size="420" fill="var(--yellow)" stroke="var(--navy)" stroke-width="14" paint-order="stroke" stroke-linejoin="round" textLength="300" lengthAdjust="spacingAndGlyphs">10</text>
    <g class="years-tag">
      <polygon points="560,208 698,208 672,262 540,262" fill="url(#gold-fill)"/>
      <text x="620" y="246" text-anchor="middle" class="sans" font-weight="800" font-style="italic" font-size="26" fill="var(--white)">Years</text>
    </g>
    <g class="anniversary-ribbon">
      <polygon points="115,340 180,330 190,388 130,400 150,372" fill="var(--red-dark)"/>
      <polygon points="665,355 600,338 592,398 650,400 640,378" fill="var(--red-dark)"/>
      <path d="M170 335 C300 360 420 330 610 320 L600 390 C420 395 300 430 185 400 Z" fill="var(--red)" stroke="var(--white)" stroke-width="3"/>
      <text x="395" y="395" text-anchor="middle" class="rounded" font-size="44" fill="var(--white)" transform="rotate(-9 395 380)">Anniversary</text>
    </g>
  </g>

  <!-- headlines -->
  <text x="430" y="548" text-anchor="middle" class="display-serif" font-size="92" fill="var(--yellow)" stroke="var(--navy)" stroke-width="4" paint-order="stroke" textLength="440" lengthAdjust="spacingAndGlyphs">CELEBRATION</text>
  <text x="424" y="600" text-anchor="middle" class="sans" font-weight="700" font-size="30" fill="var(--white)">Everyone takes part in our</text>
  <text x="424" y="704" text-anchor="middle" class="display-serif" font-size="100" fill="var(--yellow)" textLength="690" lengthAdjust="spacingAndGlyphs">GRAND PRIZE GIVEAWAY</text>

  <g class="prize-ribbon">
    <polygon points="110,718 138,731 110,746" fill="var(--red-dark)"/>
    <polygon points="740,718 712,731 740,746" fill="var(--red-dark)"/>
    <rect x="122" y="716" width="606" height="30" fill="var(--red)"/>
    <text x="425" y="738" text-anchor="middle" class="sans" font-weight="700" font-size="19" fill="var(--white)" textLength="590" lengthAdjust="spacingAndGlyphs">Your opportunity to win one of our $000’s prizes including</text>
  </g>
  <text x="424" y="782" text-anchor="middle" class="sans" font-size="28" fill="var(--white)">ONE GRAND PRIZE OF</text>
  <text x="424" y="828" text-anchor="middle" class="sans" font-weight="800" font-size="28" fill="var(--white)" textLength="666" lengthAdjust="spacingAndGlyphs">ONE YEAR CHIROPRACTIC WELLNESS CARE!!!!</text>

  <!-- prizes -->
  <g class="prize-row">
    <g class="prize prize-massage">
      <circle cx="104" cy="907" r="60" fill="var(--gold)"/>
      <circle cx="104" cy="907" r="53" fill="var(--white)"/>
      <g class="sans" text-anchor="middle" fill="var(--ink)">
        <text x="104" y="884" font-size="12.5">1 x 1 hour</text>
        <text x="104" y="899" font-size="12.5">bed massage</text>
        <circle cx="104" cy="916" r="6" fill="#2a9a9a"/>
        <text x="104" y="936" font-size="9" fill="#2a7f85">Mintleaf Massage</text>
      </g>
    </g>
    <g class="prize">
      <circle cx="230" cy="907" r="60" fill="var(--gold)"/>
      <circle cx="230" cy="907" r="53" fill="#3d3f4a" role="img" aria-label="Photo of a lumbar support cushion"/>
    </g>
    <g class="prize">
      <circle cx="355" cy="907" r="60" fill="var(--gold)"/>
      <circle cx="355" cy="907" r="53" fill="#a99278" role="img" aria-label="Photo of boxed wellness gift sets"/>
    </g>
    <g class="prize">
      <circle cx="481" cy="907" r="60" fill="var(--gold)"/>
      <circle cx="481" cy="907" r="53" fill="#2e7b78" role="img" aria-label="Photo of bottled body care products"/>
    </g>
    <g class="prize">
      <circle cx="607" cy="907" r="60" fill="var(--gold)"/>
      <circle cx="607" cy="907" r="53" fill="#1d6fd0" role="img" aria-label="Photo of blue foam rollers"/>
    </g>
    <g class="prize">
      <circle cx="733" cy="907" r="60" fill="var(--gold)"/>
      <circle cx="733" cy="907" r="53" fill="#d9c7c2" role="img" aria-label="Photo of boxed pillows"/>
    </g>
  </g>

  <!-- terms -->
  <g class="terms sans" fill="var(--white)" font-size="9.5">
    <text x="36" y="1024" font-size="10">T&amp;C’s</text>
    <g font-style="italic">
      <text x="38" y="1043">•</text>
      <text x="50" y="1043">CWC Anniversary Prize Giveaway and 10% discounts valid from</text>
      <text x="50" y="1055">1st October to 31st October 2020 only.</text>
      <text x="38" y="1073">•</text>
      <text x="50" y="1073">Receive one lucky prize draw entry for every adjustment during</text>
      <text x="50" y="1085">October (max 4 during the month).</text>
      <text x="38" y="1103">•</text>
      <text x="50" y="1103">Receive an additional lucky prize draw entry for each year you</text>
      <text x="50" y="1115">have been a client with CoreWell Chiropractic</text>
      <text x="38" y="1133">•</text>
      <text x="50" y="1133">All prizes must be collected from the clinic.</text>
      <text x="38" y="1151">•</text>
      <text x="50" y="1151">CWC decision is final</text>
    </g>
  </g>

  <!-- charity panel -->
  <g class="charity-panel">
    <path d="M430 1012 H849 V1146 H430 A67 67 0 0 1 430 1012 Z" fill="var(--white)" stroke="var(--yellow)" stroke-width="5"/>
    <circle cx="430" cy="1079" r="46" fill="none" stroke="#33a6e0" stroke-width="5"/>
    <circle cx="430" cy="1079" r="34" fill="#33a6e0" fill-opacity="0.18"/>
    <g class="sans" font-size="11.5" fill="var(--ink)">
      <text x="500" y="1040">As a thank you to Singapore, we know we would never</text>
      <text x="500" y="1056">have made it this far without the loyalty of our clients.</text>
      <text x="500" y="1072">Therefore, we will be giving back to the community and</text>
      <text x="500" y="1088">with every package purchased in October, we will buy</text>
      <text x="500" y="1104">10 meals for the hungry people in Singapore via</text>
      <text x="500" y="1120">GiveTogether and the City Food Pantry.</text>
    </g>
  </g>
</svg>
</body>
</html>
```